Allies in Wellness Groupworks- Medical Billing and Consultant Firm Business card

We need a logo design for a medical billing and healthcare consulting firm. We help physician medical practices achieve their financial objectives by providing medical billing services and other revenue cycle services. We want a business card design that is eye catching and compliments the color and design my logo. We like variations of blue colors however we are very open to other colors. We would like the services we provide listed on the back of the card.

Target Market(s)

Doctors and medical practices

Industry/Entity Type

Medical

Contact Information for Business Card

Space for logo, name, title, phone #, address, web address

Font styles to use
Serif
Sans Serif

Colors

Designer to choose colors to be used in the design.

Requirements
Must have
• Company Services listed on the back.
Should not have
• We are pretty open to all design ideas

```html
<!DOCTYPE html>
<html lang="en">
<head>
<meta charset="utf-8">
<title>Allies in Wellness Groupworks — Business Card</title>
<link rel="stylesheet" href="https://fonts.googleapis.com/css2?family=Questrial&display=swap">
<style>
  :root {
    --brand-blue: #1258a8;
    --brand-navy: #1a4f9c;
    --brand-sky: #35a3d8;
    --paper: #ffffff;
    --stage: #e9ebee;
    --ink-light: #ffffff;
  }
  * { margin: 0; padding: 0; box-sizing: border-box; }
  html, body { width: 1200px; height: 880px; overflow: hidden; }
  body {
    background: var(--stage);
    font-family: "Questrial", "Century Gothic", sans-serif;
    position: relative;
  }
  .card {
    position: absolute;
    left: 280px;
    width: 640px;
    height: 366px;
    border-radius: 18px;
    overflow: hidden;
    box-shadow: 0 6px 18px rgba(0,0,0,0.18);
  }
  .card--back { top: 44px; background: var(--brand-blue); color: var(--ink-light); }
  .card--front { top: 470px; background: var(--paper); }

  /* back */
  .back-brand {
    position: absolute; top: 96px; left: 0; right: 0;
    display: flex; align-items: center; justify-content: center; gap: 14px;
  }
  .brand-mark { width: 22px; height: 22px; border-radius: 50%; background: currentColor; flex: none; }
  .brand-name { font-size: 30px; letter-spacing: 1px; text-transform: uppercase; line-height: 1.15; }
  .services {
    position: absolute; top: 200px; left: 40px; right: 40px;
    text-align: center; font-size: 16px; line-height: 1.55; letter-spacing: 0.2px;
  }

  /* front */
  .wave { position: absolute; inset: 0; width: 640px; height: 366px; }
  .front-brand {
    position: absolute; left: 44px; top: 112px;
    display: flex; align-items: center; gap: 12px; color: var(--brand-navy);
  }
  .front-brand .brand-name { font-size: 24px; }
  .person { position: absolute; top: 30px; right: 40px; text-align: right; }
  .person-name { color: var(--brand-navy); font-size: 20px; letter-spacing: 0.5px; }
  .person-title { color: var(--brand-sky); font-size: 15px; }
  .contact {
    position: absolute; right: 26px; top: 196px;
    color: var(--ink-light); font-size: 13.5px; text-align: right; line-height: 1.45;
    font-style: normal;
  }
  .contact-row { display: flex; align-items: center; justify-content: flex-end; gap: 8px; }
  .contact-address { margin-bottom: 6px; padding-right: 28px; }
  .icon { width: 20px; height: 20px; flex: none; }
</style>
</head>
<body>

<section class="card card--back" aria-label="Card back">
  <div class="back-brand">
    <span class="brand-mark"></span>
    <span class="brand-name">Allies in Wellness<br>Groupworks</span>
  </div>
  <p class="services">
    Medical Billing | Revenue Cycle Management | Coding Audits<br>
    Practice Consulting and Provider Credentialing
  </p>
</section>

<section class="card card--front" aria-label="Card front">
  <svg class="wave" viewBox="0 0 640 366" aria-hidden="true">
    <path fill="var(--brand-blue)" d="M640 98 C520 100 435 128 390 200 C345 280 295 345 195 366 L640 366 Z"/>
    <path fill="var(--brand-navy)" d="M575 104 C475 116 410 160 365 235 C325 305 270 350 150 366 L180 366 C285 348 335 305 375 240 C420 168 480 120 600 102 Z"/>
    <path fill="var(--brand-navy)" d="M0 352 C120 356 220 345 300 300 C260 345 150 362 0 366 Z"/>
    <path fill="var(--brand-sky)" d="M0 320 C120 330 230 322 300 285 C330 268 345 248 350 230 C345 272 320 300 280 320 C210 350 110 352 0 342 Z"/>
  </svg>

  <div class="person">
    <div class="person-name">JORDAN HALE</div>
    <div class="person-title">Owner</div>
  </div>

  <div class="front-brand">
    <span class="brand-mark"></span>
    <span class="brand-name">ALLIES IN WELLNESS<br>GROUPWORKS</span>
  </div>

  <address class="contact">
    <div class="contact-address">PO Box 418 Harbor Lane<br>2nd Street Riverton</div>
    <div class="contact-row">(555) 014-2870
      <svg class="icon" viewBox="0 0 20 20"><circle cx="10" cy="10" r="9" fill="none" stroke="#fff" stroke-width="1.5"/><path d="M7 5.5 L8.6 5.5 L9.3 8 L8.2 9 C8.8 10.3 9.7 11.2 11 11.8 L12 10.7 L14.5 11.4 L14.5 13 C10 13.5 6.5 10 7 5.5 Z" fill="#fff"/></svg>
    </div>
    <div class="contact-row">hello@alliesgroupworks.com
      <svg class="icon" viewBox="0 0 20 20"><circle cx="10" cy="10" r="9" fill="none" stroke="#fff" stroke-width="1.5"/><rect x="5" y="6.5" width="10" height="7" fill="#fff"/><path d="M5 6.5 L10 10.5 L15 6.5" fill="none" stroke="var(--brand-blue)" stroke-width="1"/></svg>
    </div>
    <div class="contact-row">www.alliesgroupworks.com
      <svg class="icon" viewBox="0 0 20 20"><circle cx="10" cy="10" r="9" fill="none" stroke="#fff" stroke-width="1.5"/><circle cx="10" cy="10" r="5" fill="none" stroke="#fff" stroke-width="1.2"/><path d="M5 10 H15 M10 5 V15 M10 5 C7.5 8 7.5 12 10 15 M10 5 C12.5 8 12.5 12 10 15" fill="none" stroke="#fff" stroke-width="1"/></svg>
    </div>
  </address>
</section>

</body>
</html>
```